Small boutique home based travel agency needs a flyer design and logo

I need a flyer design for my boutique home-based travel agency that specializes in designing personalized trips to Europe, ocean and river cruises and escorted small group tours to exotic destinations.

We are travel experts, provide the best customer service in the industry and would like this promoted. Open by appointment.
Would like the flyer and logo to use a globe and I like color. Please integrate photo.

Boutique

```html
<!DOCTYPE html>
<html lang="en">
<head>
<meta charset="utf-8">
<title>Meridian Voyages – Trifold Brochure</title>
<link rel="stylesheet" href="https://fonts.googleapis.com/css2?family=Open+Sans:ital,wght@0,400;0,600;0,700;1,700&display=swap">
<style>
  :root {
    --backdrop: #8f8f8f;
    --brand-red: #cf1f2a;
    --ink: #3b3b3b;
    --ink-soft: #555555;
    --paper: #ffffff;
    --band-gray: #6d6d6d;
  }
  * { margin: 0; padding: 0; box-sizing: border-box; }
  html, body { width: 891px; height: 1200px; overflow: hidden; }
  body {
    background: linear-gradient(180deg, #9a9a9a 0%, var(--backdrop) 100%);
    font-family: "Open Sans", Arial, sans-serif;
    color: var(--ink);
    position: relative;
  }
  .sheet {
    position: absolute;
    left: 30px;
    width: 831px;
    height: 500px;
    background: var(--paper);
    box-shadow: 0 10px 24px rgba(0,0,0,.28);
    overflow: hidden;
  }
  .sheet--outside { top: 45px; }
  .sheet--inside { top: 620px; }
  .sheet svg { position: absolute; inset: 0; }
  .text { position: absolute; }

  .welcome { width: 230px; font-size: 7.6px; line-height: 1.4; color: var(--ink-soft); }
  .welcome h2 { font-size: 10.5px; font-style: italic; font-weight: 700; color: var(--ink); margin-bottom: 5px; }
  .welcome p { margin-bottom: 5px; }
  .welcome--inside { line-height: 1.35; }
  .welcome--inside p { margin-bottom: 4px; }

  .contact { width: 277px; text-align: center; }
  .contact__name { font-size: 14px; font-weight: 400; }
  .contact__email { font-size: 15px; font-weight: 700; font-style: italic; }
  .contact__phone { font-size: 20px; font-weight: 700; letter-spacing: .5px; }
  .contact__web { font-size: 12.5px; }

  .brand-name {
    display: flex; align-items: center; justify-content: center; gap: 7px;
    font-weight: 600; white-space: nowrap;
  }
  .brand-name__dot { width: 10px; height: 10px; border-radius: 50%; background: currentColor; }

  .social { display: flex; justify-content: center; gap: 5px; }
  .social span { width: 12px; height: 12px; background: currentColor; border-radius: 2px; }

  .on-red { color: var(--paper); }
  .phone-red { color: var(--brand-red); }

  .services { left: 40px; top: 62px; list-style: none; color: var(--paper); }
  .services li {
    display: flex; align-items: center; gap: 8px;
    font-size: 18px; font-weight: 700; font-style: italic; line-height: 25px;
  }
  .services svg { position: static; }
</style>
</head>
<body>

<!-- Outside of the trifold -->
<section class="sheet sheet--outside">
  <svg width="831" height="500" viewBox="0 0 831 500">
    <defs>
      <linearGradient id="sky-dusk" x1="0" y1="0" x2="0" y2="1">
        <stop offset="0" stop-color="#3f5f8f"/>
        <stop offset=".45" stop-color="#9fb6cf"/>
        <stop offset=".7" stop-color="#e0b98c"/>
        <stop offset="1" stop-color="#3d4a4f"/>
      </linearGradient>
      <linearGradient id="portrait-tone" x1="0" y1="0" x2="0" y2="1">
        <stop offset="0" stop-color="#7fa36b"/>
        <stop offset="1" stop-color="#e9e3dc"/>
      </linearGradient>
    </defs>
    <g role="img" aria-label="Coastal lookout with visitors at sunset">
      <path d="M0 0H277V255Q150 285 0 325Z" fill="url(#sky-dusk)"/>
    </g>
    <path d="M0 325Q150 285 277 255V266Q150 298 0 340Z" fill="var(--brand-red)"/>
    <path d="M0 340Q150 298 277 266V272Q150 306 0 348Z" fill="#d9d9d9"/>

    <g role="img" aria-label="Sky over the ocean at dusk">
      <path d="M277 0H554V228Q415 248 277 282Z" fill="url(#sky-dusk)"/>
    </g>
    <path d="M277 282Q415 248 554 228V500H277Z" fill="var(--brand-red)"/>

    <g role="img" aria-label="Sea stacks along the coast at sunset">
      <path d="M554 0H831V210Q700 218 554 262Z" fill="url(#sky-dusk)"/>
    </g>
    <path d="M554 262Q700 218 831 210V226Q700 232 554 276Z" fill="#6a6a6a"/>
    <path d="M554 276Q700 232 831 226V240Q700 246 554 290Z" fill="#e4e4e4"/>

    <g role="img" aria-label="Portrait of the travel agent">
      <circle cx="415" cy="248" r="62" fill="url(#portrait-tone)" stroke="#fff" stroke-width="6"/>
    </g>
  </svg>

  <div class="text welcome" style="left:28px; top:340px;">
    <h2>Welcome to Meridian Voyages!</h2>
    <p>Meridian Voyages is a full service travel agency. Our promise to our clients is to provide the best personalized customer service in the industry. We are a small agency with many years of travel experience and have the expertise to plan the travel experience that is just right for you.</p>
    <p>We can plan your family vacation or a special trip for your group, church or club.</p>
    <p>Meridian also plans and offers several escorted small group vacations each year to interesting and fun destinations.</p>
    <p>To find out how we can be of service to you, please contact us and one of our agents will gladly assist you.</p>
  </div>

  <div class="text contact on-red" style="left:277px; top:318px;">
    <div class="contact__name">Contact: Dana</div>
    <div class="contact__email">dana.meridian@mailbox.com</div>
    <div class="brand-name" style="font-size:17px; margin:12px 0 10px;"><span class="brand-name__dot"></span>Meridian Voyages</div>
    <div class="contact__phone">555-214-0376</div>
    <div class="contact__web">www.meridianvoyagesbydana.com</div>
    <div class="social" style="margin-top:6px;"><span></span><span></span></div>
  </div>

  <div class="text contact" style="left:554px; top:318px;">
    <div class="brand-name" style="font-size:22px; color:var(--ink-soft); margin-bottom:60px;"><span class="brand-name__dot" style="background:var(--brand-red);"></span>Meridian Voyages</div>
    <div class="contact__phone phone-red">555-214-0376</div>
    <div class="contact__web" style="margin-top:4px;">www.meridianvoyagesbydana.com</div>
    <div class="social" style="margin-top:6px; color:var(--ink);"><span></span><span></span></div>
  </div>
</section>

<!-- Inside of the trifold -->
<section class="sheet sheet--inside">
  <svg width="831" height="500" viewBox="0 0 831 500">
    <defs>
      <linearGradient id="cruise-hotel" x1="0" y1="0" x2="0" y2="1">
        <stop offset="0" stop-color="#8a3a22"/>
        <stop offset=".35" stop-color="#3a2a26"/>
        <stop offset=".6" stop-color="#b0623a"/>
        <stop offset="1" stop-color="#d8b48e"/>
      </linearGradient>
      <linearGradient id="ship-sunset" x1="0" y1="0" x2="0" y2="1">
        <stop offset="0" stop-color="#c24a1e"/>
        <stop offset=".35" stop-color="#3a2b2a"/>
        <stop offset=".65" stop-color="#5a4a48"/>
        <stop offset="1" stop-color="#e0904a"/>
      </linearGradient>
      <linearGradient id="center-tint" x1="0" y1="0" x2="0" y2="1">
        <stop offset="0" stop-color="#e8d6cf"/>
        <stop offset=".55" stop-color="#f3ece8"/>
        <stop offset="1" stop-color="#ffffff"/>
      </linearGradient>
    </defs>
    <g role="img" aria-label="Cruise ship at sunset above a warmly lit hotel room">
      <rect x="0" y="0" width="277" height="500" fill="url(#cruise-hotel)"/>
    </g>
    <path d="M0 60L277 40V140L0 150Z" fill="#262626" opacity=".85"/>
    <path d="M0 185Q150 170 277 210V222Q150 184 0 198Z" fill="var(--brand-red)"/>

    <rect x="277" y="0" width="277" height="500" fill="url(#center-tint)"/>

    <g role="img" aria-label="Illuminated cruise ship at dusk above a couple in beach chairs at sunset">
      <rect x="554" y="0" width="277" height="500" fill="url(#ship-sunset)"/>
    </g>
    <path d="M554 300Q700 250 831 240V256Q700 266 554 316Z" fill="#bdbdbd"/>

    <g stroke="#fff" stroke-width="6">
      <g role="img" aria-label="Tropical beach with palm tree and hammock">
        <circle cx="185" cy="262" r="62" fill="#5fb5d8"/>
      </g>
      <g role="img" aria-label="Horseback ride through shallow water">
        <circle cx="335" cy="305" r="62" fill="#4f7a55"/>
      </g>
      <g role="img" aria-label="Kayaking on a river">
        <circle cx="510" cy="300" r="62" fill="#5f8f8a"/>
      </g>
      <g role="img" aria-label="Resort courtyard with fountains">
        <circle cx="670" cy="228" r="62" fill="#6f7fa8"/>
      </g>
    </g>
  </svg>

  <ul class="text services">
    <li><svg width="16" height="14" viewBox="0 0 16 14"><path d="M2 7L6 11L14 2" fill="none" stroke="#fff" stroke-width="2.6"/></svg>Cruises</li>
    <li><svg width="16" height="14" viewBox="0 0 16 14"><path d="M2 7L6 11L14 2" fill="none" stroke="#fff" stroke-width="2.6"/></svg>Tours</li>
    <li><svg width="16" height="14" viewBox="0 0 16 14"><path d="M2 7L6 11L14 2" fill="none" stroke="#fff" stroke-width="2.6"/></svg>Hotels</li>
  </ul>

  <div class="text" style="left:277px; top:36px; width:277px;">
    <div class="brand-name" style="font-size:20px; color:var(--ink-soft);"><span class="brand-name__dot" style="background:var(--brand-red);"></span>Meridian Voyages</div>
  </div>

  <div class="text welcome welcome--inside" style="left:300px; top:72px;">
    <h2 style="color:var(--brand-red);">Welcome to Meridian Voyages!</h2>
    <p>Meridian Voyages is a full service travel agency. Our promise to our clients is to provide the best personalized customer service in the industry. We are a small agency with many years of travel experience and have the expertise to plan the travel experience that is just right for you.</p>
    <p>We can plan your family vacation or a special trip for your group, church or club.</p>
    <p>Meridian also plans and offers several escorted small group vacations each year to interesting and fun destinations.</p>
    <p>To find out how we can be of service to you, please contact us and one of our agents will gladly assist you.</p>
  </div>

  <div class="text contact" style="left:277px; top:374px; color:var(--ink);">
    <div class="contact__name">Contact: Dana</div>
    <div class="contact__email" style="margin-top:4px;">dana.meridian@mailbox.com</div>
    <div class="contact__phone phone-red" style="margin-top:2px;">555-214-0376</div>
    <div class="contact__web">www.meridianvoyagesbydana.com</div>
  </div>
</section>

</body>
</html>
```